Whale Watching Voucher(ticket) Layout

Tidalroam.com.au would like a new design for their existing vouchers (tickets) being issued when a customer completes a purchase.
These vouchers are to be issued from within Salesforce CRM using Conga Composer (don't worry about that, we'll handle that) but that does mean that the voucher template needs to be designed and provided in Microsoft Word. The voucher will be sent via an email and we require a HTML email design also.
The following fields need to be included on the email/Voucher:
BOOKING CONFIRMATION NUMBER (e&v)
First Name (e&v)
Tour Name (e&v)
Tour Operator Name (e&v)
Telephone Contact (e&v)
Departure Date (e&v)
Party Name (e&v)
Adults Tickets (v)
Concession Tickets (v)
Child Tickets (v)
Infant Tickets (v)
Pickup Location (v)
Pickup Time (v)
Boarding Place (v)
Boarding Time (v)
Departure Time (v)
Return Time (v)
Terms and conditions (e&v) - this is quite a long description
What to Bring (v) - this is quite a long description
What to do if the Pick-up is more than 10 mins late (v) - this is a long description
What to do if you're late (v) - this is quite a long description
Booking Terms and Conditions
{!Opportunity.Tour_Terms_and_Conditions_PG1__c}
FREECALL 1800 437 962 (Australia)
International +61 7 5926 8174
Skype journeymoss
(e&v indicate fields to be included on the Email and the Voucher)
(v indicate fields to be included on the Voucher only)
Updates
Project Deadline Extended
Reason: I realised the original Deadline didn't take weekends into account so have extended it to the end of this week. The Whale season is well underway so need to have it completed by Friday. Thanks all for your efforts.
I uploaded the current (text based) samples of the email & voucher that we are hoping you are going to be able to redesign for us.
Sorry for lack of feedback, I got caught up on another project. We are reviewing the designs tomorrow and will get back to you all.
Target Market(s)
Mid market Australian and International Tourists
Industry/Entity Type
Purchase
Requirements
Must have
- Consistency with existing Tidalroam.com.au & coralpath.com.au branding.
The Voucher should be designed to be printed out on a single A4 sheet.
Nice to have
- It would be good to have a paragraph/section referencing the coralpath.com.au logo and website on the email (not the voucher).
Any recommendation for additional information/fields that should/could be included not listed above will be gratefully received.
Happy for you to reword the labels to make them more friendly.

```html
<!DOCTYPE html>
<html lang="en">
<head>
<meta charset="utf-8">
<title>Tidalroam Tours – Booking Voucher</title>
<link rel="stylesheet" href="https://fonts.googleapis.com/css2?family=Source+Sans+3:wght@400;600;700&display=swap">
<style>
  :root {
    --brand-blue: #1f86c6;
    --brand-teal: #179a9b;
    --label-grey: #9a9a9a;
    --body-grey: #6b6b6b;
    --field-sand: #efe2c8;
    --field-shadow: #d9c8a6;
    --footer-sand: #f4edd9;
    --footer-line: #d8c9a4;
    --paper: #ffffff;
  }
  * { box-sizing: border-box; margin: 0; padding: 0; }
  html, body { width: 849px; height: 1200px; overflow: hidden; background: var(--paper); }
  body { font-family: "Source Sans 3", "Myriad Pro", Arial, sans-serif; position: relative; }

  .brand { position: absolute; left: 62px; top: 52px; display: flex; align-items: center; gap: 14px; }
  .brand-dot { width: 54px; height: 54px; border-radius: 50%; background: var(--brand-teal); }
  .brand-name { font-size: 34px; font-weight: 700; color: var(--brand-teal); letter-spacing: 1px; }

  .voucher-title { position: absolute; left: 84px; top: 118px; font-size: 31px; font-weight: 700; color: var(--brand-blue); letter-spacing: 0.3px; }

  .field-label { position: absolute; font-size: 20px; color: var(--label-grey); text-align: right; line-height: 34px; white-space: nowrap; }
  .field { position: absolute; height: 34px; background: var(--field-sand); border-radius: 3px; box-shadow: inset 0 -2px 0 var(--field-shadow); }
  .field.select::after { content: ""; position: absolute; right: 12px; top: 14px; border-left: 6px solid transparent; border-right: 6px solid transparent; border-top: 7px solid #a89a80; }

  .submit { position: absolute; left: 680px; top: 664px; width: 108px; height: 36px; background: var(--brand-teal); color: #fff; border-radius: 4px; font-size: 20px; font-weight: 600; text-align: center; line-height: 36px; box-shadow: 0 2px 0 #0f7474; }

  .info { position: absolute; left: 100px; width: 660px; }
  .info h2 { font-size: 20px; font-weight: 700; color: var(--brand-blue); margin-bottom: 6px; }
  .info p { font-size: 16px; line-height: 21px; color: var(--body-grey); }

  .contact-bar { position: absolute; left: 0; top: 1134px; width: 849px; height: 66px; background: var(--footer-sand); border-top: 2px solid var(--footer-line); display: flex; align-items: center; justify-content: center; gap: 12px; font-size: 17px; color: var(--brand-teal); }
  .contact-bar .sep { color: var(--footer-line); }
</style>
</head>
<body>
  <div class="brand">
    <span class="brand-dot"></span>
    <span class="brand-name">TIDALROAM</span>
  </div>

  <h1 class="voucher-title">BOOKING CONFIRMATION NUMBER</h1>

  <!-- traveller details -->
  <div class="field-label" style="right:611px; top:181px;">First Name</div>
  <div class="field" style="left:246px; top:181px; width:542px;"></div>
  <div class="field-label" style="right:611px; top:229px;">Tour Name</div>
  <div class="field" style="left:246px; top:229px; width:542px;"></div>
  <div class="field-label" style="right:611px; top:277px;">Tour Operator Name</div>
  <div class="field" style="left:246px; top:277px; width:542px;"></div>
  <div class="field-label" style="right:611px; top:325px;">Telephone Contact</div>
  <div class="field" style="left:246px; top:325px; width:542px;"></div>
  <div class="field-label" style="right:611px; top:373px;">Departure Date</div>
  <div class="field" style="left:246px; top:373px; width:542px;"></div>
  <div class="field-label" style="right:611px; top:421px;">Party Name</div>
  <div class="field" style="left:246px; top:421px; width:542px;"></div>

  <!-- tickets and times -->
  <div class="field-label" style="right:611px; top:470px;">Adults Tickets</div>
  <div class="field select" style="left:246px; top:470px; width:128px;"></div>
  <div class="field-label" style="right:311px; top:470px;">Concession Tickets</div>
  <div class="field select" style="left:546px; top:470px; width:118px;"></div>

  <div class="field-label" style="right:611px; top:516px;">Child Tickets</div>
  <div class="field select" style="left:246px; top:516px; width:128px;"></div>
  <div class="field-label" style="right:311px; top:516px;">Infant Tickets</div>
  <div class="field select" style="left:546px; top:516px; width:118px;"></div>

  <div class="field-label" style="right:611px; top:566px;">Pickup Location</div>
  <div class="field select" style="left:246px; top:566px; width:136px;"></div>
  <div class="field-label" style="right:311px; top:566px;">Pickup Time</div>
  <div class="field select" style="left:546px; top:566px; width:118px;"></div>

  <div class="field-label" style="right:611px; top:616px;">Boarding Place</div>
  <div class="field select" style="left:246px; top:616px; width:136px;"></div>
  <div class="field-label" style="right:311px; top:616px;">Boarding Time</div>
  <div class="field select" style="left:546px; top:616px; width:118px;"></div>

  <div class="field-label" style="right:611px; top:665px;">Departure Time</div>
  <div class="field select" style="left:246px; top:665px; width:136px;"></div>
  <div class="field-label" style="right:311px; top:665px;">Return Time</div>
  <div class="field select" style="left:546px; top:665px; width:118px;"></div>

  <div class="submit">Submit</div>

  <section class="info" style="top:748px;">
    <h2>Terms and conditions</h2>
    <p>Sed ut perspiciatis unde omnis iste natus error sit voluptatem accusantium doloremque laudantium, totam rem aperiam, eaque ipsa quae ab illo inventore veritatis et quasi architecto beatae vitae dicta sunt explicabo.</p>
  </section>
  <section class="info" style="top:846px;">
    <h2>What to Bring</h2>
    <p>Sed ut perspiciatis unde omnis iste natus error sit voluptatem accusantium doloremque laudantium, totam rem aperiam</p>
  </section>
  <section class="info" style="top:940px;">
    <h2>What to do if the Pick-up is more than 10 mins late</h2>
    <p>Sed ut perspiciatis unde omnis iste natus error sit voluptatem accusantium doloremque laudantium, totam rem aperiam</p>
  </section>
  <section class="info" style="top:1028px;">
    <h2>What to do if you're late</h2>
    <p>Sed ut perspiciatis unde omnis iste natus error sit voluptatem accusantium doloremque laudantium, totam rem aperiam</p>
  </section>

  <footer class="contact-bar">
    <span>FREECALL 1800 437 962 (Australia)</span>
    <span class="sep">|</span>
    <span>International +61 7 5926 8174</span>
    <span class="sep">|</span>
    <span>Skype journeymoss</span>
  </footer>
</body>
</html>
```